The next stage in our 106 year history in Specialised Stationery

We need a business card design(which is also adaptable for our general stationery) to suit the changing face of our business. Harlow, an Australian company has been the leader in its category since 1907. We design and print various books required by small business to comply with government legislation in regards to keeping records. Accountancy, Payroll, Vehicle usage recording, Firearms registration etc. The Harlow logo a blue diamond is one of the best known in our industry. As manual recording has declined in the last few years we have diversified into other areas: Safety Apparel, Personal Protective Equipment (PPE) and web based software for bookkeeping and Customer Relationship management(CRM). Separate logos have been adopted for each of these being: Harlow Systems, Harlow Safety, Harlow Apparel and Harlow Software each with same diamond but different colour background. This has made it easy to identify the different sectors but difficult to bring together for a Corporate identity in Business cards etc. We are looking to bring all logos together (not one logo) but still allow the logo to depict the diversity of our offering, while still being able to have a category specific logo for each of the divisions. All products go through the same distribution channel, Office Products. The final design should depict an old established company well, known and trusted but leaping forward and still retaining same values they have come to trust.

Target Market(s)

Micro to small business companies generally who employ 20 or less people.

Industry/Entity Type

Small Business

Requirements
Must have
• The diamonds are well recognised and the new design should retain the integrity of them.

```html
<!DOCTYPE html>
<html lang="en">
<head>
<meta charset="utf-8">
<title>Harlow Business Card</title>
<link rel="stylesheet" href="https://fonts.googleapis.com/css2?family=Arimo:wght@400;700&display=swap">
<style>
  :root {
    --bg: #e9e9e7;
    --red: #c8202f;
    --green: #45b046;
    --blue: #0a67b4;
    --orange: #e4582a;
    --white: #ffffff;
    --grey-light: #f4f4f4;
    --grey-mid: #d6d6d6;
    --ink-blue: #1a5fb0;
  }
  * { box-sizing: border-box; margin: 0; padding: 0; }
  html, body {
    width: 1200px; height: 900px; overflow: hidden;
    background: var(--bg);
    font-family: "Arimo", Arial, sans-serif;
  }
  .stage {
    position: relative; width: 1200px; height: 900px;
  }
  .card {
    position: absolute; left: 300px; width: 600px; height: 367px;
    overflow: hidden;
    box-shadow: 0 6px 18px rgba(0,0,0,0.18);
  }
  .card-back { top: 58px; }
  .card-front { top: 475px; }

  /* Back */
  .quilt {
    position: absolute; inset: 0;
    background: linear-gradient(135deg, var(--grey-mid) 0%, var(--grey-light) 45%, var(--white) 70%, var(--grey-mid) 100%);
  }
  .division {
    position: absolute; display: flex; align-items: center; gap: 8px;
    font-weight: 700; font-size: 16px; letter-spacing: 0.5px; text-transform: uppercase;
  }
  .division .mark { width: 14px; height: 14px; }
  .division-software { left: 120px; top: 105px; color: var(--red); }
  .division-software .mark { background: var(--red); }
  .division-apparel { left: 350px; top: 75px; color: var(--green); }
  .division-apparel .mark { background: var(--green); }
  .division-systems { left: 145px; top: 225px; color: var(--blue); }
  .division-systems .mark { background: var(--blue); }
  .division-safety { left: 375px; top: 195px; color: var(--orange); }
  .division-safety .mark { background: var(--orange); }
  .back-name {
    position: absolute; left: 0; right: 0; top: 152px; text-align: center;
    font-weight: 700; font-size: 22px; color: var(--ink-blue); letter-spacing: 0.5px;
  }

  /* Front */
  .panels { position: absolute; inset: 0; }
  .front-text { position: absolute; color: var(--white); }
  .person { left: 24px; top: 22px; }
  .person-name { font-weight: 700; font-size: 24px; letter-spacing: 0.4px; }
  .person-role { font-size: 12px; margin-top: 4px; }
  .online { left: 378px; top: 26px; font-size: 14px; line-height: 20px; letter-spacing: 0.6px; }
  .phones { left: 24px; top: 258px; font-size: 14px; line-height: 20px; letter-spacing: 0.6px; }
  .address { left: 300px; top: 290px; font-size: 14px; line-height: 20px; letter-spacing: 0.3px; text-transform: uppercase; }
  .label { display: inline-block; width: 26px; }
  .brand {
    position: absolute; left: 240px; top: 168px;
    display: flex; align-items: center; gap: 10px;
    color: var(--white); font-weight: 700; font-size: 34px; letter-spacing: 1px;
  }
  .brand .mark { width: 16px; height: 16px; background: var(--white); }
</style>
</head>
<body>
<main class="stage">
  <section class="card card-back">
    <div class="quilt" role="img" aria-label="Soft grey quilted diamond pattern background"></div>
    <div class="division division-software"><span class="mark"></span>Harlow Software</div>
    <div class="division division-apparel"><span class="mark"></span>Harlow Apparel</div>
    <div class="back-name">HARLOW</div>
    <div class="division division-systems"><span class="mark"></span>Harlow Systems</div>
    <div class="division division-safety"><span class="mark"></span>Harlow Safety</div>
  </section>

  <section class="card card-front">
    <svg class="panels" width="600" height="367" viewBox="0 0 600 367" aria-hidden="true">
      <polygon points="0,0 350,0 310,190 0,175" fill="var(--red)"/>
      <polygon points="350,0 600,0 600,215 310,190" fill="var(--green)"/>
      <polygon points="310,190 600,215 600,367 270,367" fill="var(--orange)"/>
      <polygon points="0,175 310,190 270,367 0,367" fill="var(--blue)"/>
    </svg>
    <div class="front-text person">
      <div class="person-name">DANIEL MERCER</div>
      <div class="person-role">Director</div>
    </div>
    <div class="front-text online">
      <div><span class="label">E:</span>dmercer@harlow.com.au</div>
      <div><span class="label">W:</span>www.harlow.com.au</div>
    </div>
    <div class="brand"><span class="mark"></span>HARLOW</div>
    <div class="front-text phones">
      <div><span class="label">T:</span>61 2 9400 2815</div>
      <div><span class="label">F:</span>61 2 9400 2816</div>
      <div><span class="label">M:</span>0400 118 372</div>
    </div>
    <div class="front-text address">
      <div>Harlow Pty Limited</div>
      <div>Unit 4, 72 Kingsway Road,</div>
      <div>Kelvin Park, NSW 2218</div>
    </div>
  </section>
</main>
</body>
</html>
```